Make it cool to work near where you are...

Calling all creatives - create the ultimate cool card for people who want to cut their commute.

Here at TilloPod we've got what can best be described as an Marlin pass for desks - and we want to brighten up the wallets of our most loyal users.

So, pitch us your ideas and you might see your design on cards being flashed across the country - and we've thrown in a bit of cash too.

Do see our brief card guidelines - with a couple of past examples thrown in.

Industry/Entity Type

Cash

```html
<!DOCTYPE html>
<html lang="en">
<head>
<meta charset="utf-8">
<title>TilloPod Card</title>
<link rel="stylesheet" href="https://fonts.googleapis.com/css2?family=Open+Sans:wght@400;700&display=swap">
<style>
  :root {
    --ink: #111111;
    --paper: #ffffff;
    --band: #463d3e;
    --house-dark: #3f3738;
    --roof-warm: #e0663f;
    --roof-pink: #d93a78;
    --roof-plum: #7d3f80;
  }
  html, body {
    margin: 0;
    padding: 0;
    width: 1200px;
    height: 754px;
    overflow: hidden;
    background: var(--paper);
  }
  .card {
    position: relative;
    width: 1200px;
    height: 754px;
    overflow: hidden;
    background: var(--paper);
    font-family: "Open Sans", sans-serif;
  }
  .street-pattern {
    position: absolute;
    left: 0;
    top: 0;
    width: 1200px;
    height: 631px;
    background:
      linear-gradient(180deg, rgba(224,102,63,0.55) 0%, rgba(63,55,56,0) 35%),
      linear-gradient(90deg, var(--roof-warm) 0%, var(--house-dark) 25%, var(--roof-plum) 55%, var(--roof-pink) 75%, var(--house-dark) 100%);
    opacity: 0.9;
  }
  .card-number {
    position: absolute;
    left: 104px;
    top: 450px;
    padding: 0 8px;
    background: var(--paper);
    color: var(--ink);
    font-size: 36px;
    line-height: 50px;
    letter-spacing: 0.5px;
  }
  .footer-band {
    position: absolute;
    left: 0;
    top: 631px;
    width: 1200px;
    height: 123px;
    background: var(--band);
  }
  .brand-tab {
    position: absolute;
    left: 938px;
    top: 560px;
    width: 165px;
    height: 71px;
    background: var(--band);
    display: flex;
    align-items: center;
    justify-content: center;
  }
  .brand-name {
    color: var(--paper);
    font-weight: 700;
    font-size: 32px;
  }
  .web-address {
    position: absolute;
    left: 0;
    width: 1200px;
    top: 655px;
    text-align: center;
    color: var(--paper);
    font-size: 38px;
    line-height: 60px;
  }
</style>
</head>
<body>
  <div class="card">
    <div class="street-pattern" role="img" aria-label="Pattern of dark grey houses and tower blocks with multicoloured roofs in orange, red, pink, purple and teal"></div>
    <div class="card-number">0123 456 789 101</div>
    <div class="footer-band"></div>
    <div class="brand-tab"><span class="brand-name">TilloPod</span></div>
    <div class="web-address">www.tillopod.com</div>
  </div>
</body>
</html>
```